Custom Meal Plan Template

I would like to get a designed template for a custom meal plan, including shopping list, instructions, pictures spots, a information page, a spot for ingredients and a month/week plan for food.
This i going to be used by a enterprise Hollinbrook Vale Corp.
I uploaded our logo that i would like to have somewhere.

Standard A4 Page, no required number of pages, but at least page for recipie, one for the shopping list, one for month/week plan and 1 for information page.

```html
<!DOCTYPE html>
<html lang="en">
<head>
<meta charset="utf-8">
<title>Meal Plan Booklet – Hollinbrook Vale Corp.</title>
<link href="https://fonts.googleapis.com/css2?family=Montserrat:wght@700;800&family=Open+Sans:wght@400;600;700&display=swap" rel="stylesheet">
<style>
  :root {
    --backdrop: #e9edf1;
    --paper: #ffffff;
    --ink: #111111;
    --body: #4a4a4a;
    --muted: #9a9a9a;
    --orange: #ef9a62;
    --purple: #7b5ea7;
    --cell: #e6e6e6;
    --rule: #cfcfcf;
  }
  * { box-sizing: border-box; margin: 0; padding: 0; }
  html, body { width: 1200px; height: 900px; overflow: hidden; }
  body {
    background: var(--backdrop);
    font-family: "Open Sans", Arial, sans-serif;
    color: var(--body);
    display: flex; align-items: center; justify-content: center;
  }
  .spread { display: flex; gap: 6px; }
  .page {
    position: relative;
    width: 500px; height: 707px;
    background: var(--paper);
    box-shadow: 0 2px 10px rgba(0,0,0,.08);
  }
  .page-title {
    font-family: "Montserrat", Arial, sans-serif;
    font-weight: 800; font-size: 24px; color: var(--ink);
    letter-spacing: .2px;
  }
  .title-dash { width: 26px; height: 3px; background: var(--ink); margin-top: 14px; }
  .brand {
    position: absolute; right: 22px; bottom: 18px;
    font-size: 7px; font-weight: 600; color: var(--purple);
  }

  /* ---------- Meal plan page ---------- */
  .plan { padding: 54px 40px 0 44px; }
  .plan-grid {
    margin-top: 42px;
    display: grid;
    grid-template-columns: repeat(7, 58px);
    column-gap: 2px;
  }
  .week { display: contents; }
  .day-head {
    height: 22px; margin-top: 14px;
    display: flex; align-items: center; justify-content: center;
    font-family: "Montserrat", Arial, sans-serif; font-weight: 700;
    font-size: 7px; color: #fff;
  }
  .week:first-child .day-head { margin-top: 0; }
  .week--orange .day-head { background: var(--orange); }
  .week--purple .day-head { background: var(--purple); }
  .day-meals {
    height: 62px; margin-top: 2px;
    background: var(--cell);
    font-size: 5.5px; line-height: 1.4; text-align: center;
    padding-top: 8px; color: #555;
  }
  .plan-note {
    grid-column: 4 / 8; grid-row: span 2;
    margin-top: 14px; padding-left: 6px;
    font-size: 6.5px; line-height: 1.55; color: var(--body);
  }

  /* ---------- Recipe page ---------- */
  .recipe { padding: 54px 30px 0 26px; }
  .recipe-header { display: flex; justify-content: space-between; align-items: flex-start; }
  .recipe-name {
    width: 272px; height: 28px; margin-top: -2px;
    background: var(--purple); color: #fff;
    font-family: "Montserrat", Arial, sans-serif; font-weight: 800; font-size: 12px;
    display: flex; align-items: center; justify-content: center;
  }
  .recipe-top { display: flex; gap: 20px; margin-top: 22px; }
  .dish-photo { width: 200px; height: 200px; flex: none; margin-top: 28px; }
  .section-label {
    font-family: "Montserrat", Arial, sans-serif; font-weight: 700;
    font-size: 9px; color: var(--muted); letter-spacing: .3px;
    padding-bottom: 6px; border-bottom: 1px solid var(--rule);
  }
  .ingredients { flex: 1; }
  .ingredients ul { list-style: none; margin-top: 8px; }
  .ingredients li {
    position: relative; padding-left: 9px;
    font-size: 6.4px; line-height: 1.5; margin-bottom: 2.5px;
  }
  .ingredients li::before {
    content: ""; position: absolute; left: 1px; top: 3.5px;
    width: 3px; height: 3px; border-radius: 50%; background: var(--body);
  }
  .method { margin-top: 20px; }
  .method ol { margin-top: 9px; padding-left: 12px; }
  .method li { font-size: 6.6px; line-height: 1.6; margin-bottom: 6px; }
  .tip {
    margin-top: 40px; width: 360px; height: 30px;
    background: var(--orange); color: #fff;
    font-size: 6px; line-height: 1.5; padding: 6px 8px;
  }
  .tip strong { font-weight: 700; }
</style>
</head>
<body>
  <div class="spread">

    <section class="page plan">
      <h1 class="page-title">MONTHLY MEAL PLAN</h1>
      <div class="title-dash"></div>

      <div class="plan-grid">
        <div class="week week--orange">
          <div class="day-head" style="grid-row:1">DAY 01</div><div class="day-head" style="grid-row:1">DAY 02</div><div class="day-head" style="grid-row:1">DAY 03</div><div class="day-head" style="grid-row:1">DAY 04</div><div class="day-head" style="grid-row:1">DAY 05</div><div class="day-head" style="grid-row:1">DAY 06</div><div class="day-head" style="grid-row:1">DAY 07</div>
          <div class="day-meals" style="grid-row:2">Eggs on toast<br>Banana<br>Chicken<br>Fruit Salad<br>Salmon</div><div class="day-meals" style="grid-row:2">Eggs on toast<br>Banana<br>Chicken<br>Fruit Salad<br>Salmon</div><div class="day-meals" style="grid-row:2">Eggs on toast<br>Banana<br>Chicken<br>Fruit Salad<br>Salmon</div><div class="day-meals" style="grid-row:2">Eggs on toast<br>Banana<br>Chicken<br>Fruit Salad<br>Salmon</div><div class="day-meals" style="grid-row:2">Eggs on toast<br>Banana<br>Chicken<br>Fruit Salad<br>Salmon</div><div class="day-meals" style="grid-row:2">Eggs on toast<br>Banana<br>Chicken<br>Fruit Salad<br>Salmon</div><div class="day-meals" style="grid-row:2">Eggs on toast<br>Banana<br>Chicken<br>Fruit Salad<br>Salmon</div>
        </div>
        <div class="week week--purple">
          <div class="day-head" style="grid-row:3">DAY 08</div><div class="day-head" style="grid-row:3">DAY 09</div><div class="day-head" style="grid-row:3">DAY 10</div><div class="day-head" style="grid-row:3">DAY 11</div><div class="day-head" style="grid-row:3">DAY 12</div><div class="day-head" style="grid-row:3">DAY 13</div><div class="day-head" style="grid-row:3">DAY 14</div>
          <div class="day-meals" style="grid-row:4">Eggs on toast<br>Banana<br>Chicken<br>Fruit Salad<br>Salmon</div><div class="day-meals" style="grid-row:4">Eggs on toast<br>Banana<br>Chicken<br>Fruit Salad<br>Salmon</div><div class="day-meals" style="grid-row:4">Eggs on toast<br>Banana<br>Chicken<br>Fruit Salad<br>Salmon</div><div class="day-meals" style="grid-row:4">Eggs on toast<br>Banana<br>Chicken<br>Fruit Salad<br>Salmon</div><div class="day-meals" style="grid-row:4">Eggs on toast<br>Banana<br>Chicken<br>Fruit Salad<br>Salmon</div><div class="day-meals" style="grid-row:4">Eggs on toast<br>Banana<br>Chicken<br>Fruit Salad<br>Salmon</div><div class="day-meals" style="grid-row:4">Eggs on toast<br>Banana<br>Chicken<br>Fruit Salad<br>Salmon</div>
        </div>
        <div class="week week--orange">
          <div class="day-head" style="grid-row:5">DAY 15</div><div class="day-head" style="grid-row:5">DAY 16</div><div class="day-head" style="grid-row:5">DAY 17</div><div class="day-head" style="grid-row:5">DAY 18</div><div class="day-head" style="grid-row:5">DAY 19</div><div class="day-head" style="grid-row:5">DAY 20</div><div class="day-head" style="grid-row:5">DAY 21</div>
          <div class="day-meals" style="grid-row:6">Eggs on toast<br>Banana<br>Chicken<br>Fruit Salad<br>Salmon</div><div class="day-meals" style="grid-row:6">Eggs on toast<br>Banana<br>Chicken<br>Fruit Salad<br>Salmon</div><div class="day-meals" style="grid-row:6">Eggs on toast<br>Banana<br>Chicken<br>Fruit Salad<br>Salmon</div><div class="day-meals" style="grid-row:6">Eggs on toast<br>Banana<br>Chicken<br>Fruit Salad<br>Salmon</div><div class="day-meals" style="grid-row:6">Eggs on toast<br>Banana<br>Chicken<br>Fruit Salad<br>Salmon</div><div class="day-meals" style="grid-row:6">Eggs on toast<br>Banana<br>Chicken<br>Fruit Salad<br>Salmon</div><div class="day-meals" style="grid-row:6">Eggs on toast<br>Banana<br>Chicken<br>Fruit Salad<br>Salmon</div>
        </div>
        <div class="week week--purple">
          <div class="day-head" style="grid-row:7">DAY 22</div><div class="day-head" style="grid-row:7">DAY 23</div><div class="day-head" style="grid-row:7">DAY 24</div><div class="day-head" style="grid-row:7">DAY 25</div><div class="day-head" style="grid-row:7">DAY 26</div><div class="day-head" style="grid-row:7">DAY 27</div><div class="day-head" style="grid-row:7">DAY 28</div>
          <div class="day-meals" style="grid-row:8">Eggs on toast<br>Banana<br>Chicken<br>Fruit Salad<br>Salmon</div><div class="day-meals" style="grid-row:8">Eggs on toast<br>Banana<br>Chicken<br>Fruit Salad<br>Salmon</div><div class="day-meals" style="grid-row:8">Eggs on toast<br>Banana<br>Chicken<br>Fruit Salad<br>Salmon</div><div class="day-meals" style="grid-row:8">Eggs on toast<br>Banana<br>Chicken<br>Fruit Salad<br>Salmon</div><div class="day-meals" style="grid-row:8">Eggs on toast<br>Banana<br>Chicken<br>Fruit Salad<br>Salmon</div><div class="day-meals" style="grid-row:8">Eggs on toast<br>Banana<br>Chicken<br>Fruit Salad<br>Salmon</div><div class="day-meals" style="grid-row:8">Eggs on toast<br>Banana<br>Chicken<br>Fruit Salad<br>Salmon</div>
        </div>
        <div class="week week--orange">
          <div class="day-head" style="grid-row:9;grid-column:1">DAY 29</div><div class="day-head" style="grid-row:9;grid-column:2">DAY 30</div><div class="day-head" style="grid-row:9;grid-column:3">DAY 31</div>
          <div class="day-meals" style="grid-row:10;grid-column:1">Eggs on toast<br>Banana<br>Chicken<br>Fruit Salad<br>Salmon</div><div class="day-meals" style="grid-row:10;grid-column:2">Eggs on toast<br>Banana<br>Chicken<br>Fruit Salad<br>Salmon</div><div class="day-meals" style="grid-row:10;grid-column:3">Eggs on toast<br>Banana<br>Chicken<br>Fruit Salad<br>Salmon</div>
        </div>
        <p class="plan-note" style="grid-row:9 / 11">Lorem ipsum dolor sit amet, consectetur adipiscing elit, sed do eiusmod tempor incididunt ut labore et dolore magna aliqua. Ut enim ad minim veniam, quis nostrud exercitation ullamco laboris nisi ut aliquip ex ea commodo consequat. Duis aute irure dolor in reprehenderit in voluptate velit esse cillum dolore eu fugiat nulla pariatur.</p>
      </div>

      <span class="brand">Hollinbrook Vale Corp.</span>
    </section>

    <section class="page recipe">
      <div class="recipe-header">
        <div>
          <h1 class="page-title">RECIPE #1</h1>
          <div class="title-dash"></div>
        </div>
        <div class="recipe-name">CHICKEN SATAY SALAD</div>
      </div>

      <div class="recipe-top">
        <svg class="dish-photo" viewBox="0 0 200 200" role="img" aria-label="Photo of chicken satay salad in a bowl">
          <defs>
            <radialGradient id="dishTone" cx="50%" cy="50%" r="50%">
              <stop offset="0%" stop-color="#d9a36a"/>
              <stop offset="60%" stop-color="#a7b865"/>
              <stop offset="100%" stop-color="#6f8f4a"/>
            </radialGradient>
          </defs>
          <circle cx="100" cy="100" r="97" fill="var(--purple)"/>
          <circle cx="100" cy="100" r="90" fill="url(#dishTone)"/>
        </svg>

        <div class="ingredients">
          <h2 class="section-label">INGREDIENTS</h2>
          <ul>
            <li>1 tbsp tamari</li>
            <li>1 tsp medium curry powder</li>
            <li>¼ tsp ground cumin</li>
            <li>1 garlic clove, finely grated</li>
            <li>1 tsp clear honey</li>
            <li>2 skinless chicken breast fillets (or use turkey breast)</li>
            <li>1 tbsp crunchy peanut butter (choose a sugar-free version with no palm oil, if possible)</li>
            <li>1 tbsp sweet chilli sauce</li>
            <li>1 tbsp lime juice</li>
            <li>a little sunflower oil, for wiping the pan</li>
            <li>2 Little Gem lettuce hearts, cut into wedges</li>
            <li>¼ cucumber, halved and sliced</li>
            <li>1 banana shallot, halved and thinly sliced</li>
            <li>generous handful coriander</li>
            <li>chopped seeds from ½ pomegranate</li>
          </ul>
        </div>
      </div>

      <div class="method">
        <h2 class="section-label">METHOD</h2>
        <ol>
          <li>Pour the tamari into a large dish and stir in the curry powder, cumin, garlic and honey. Mix well. Slice the chicken breasts in half horizontally to make 4 fillets in total, then add to the marinade and mix well to coat. Set aside in the fridge for at least 1 hr, or overnight, to allow the flavours to penetrate the chicken.</li>
          <li>Meanwhile, mix the peanut butter with the chilli sauce, lime juice, and 1 tbsp water to make a spoonable sauce. When ready to cook the chicken, wipe a large non-stick frying pan with a little oil. Add the chicken and cook, covered with a lid, for 5-6 mins on a medium heat, turning the fillets over for the last min, until cooked but still moist. Set aside, covered, to rest for a few mins.</li>
          <li>While the chicken rests, toss the lettuce wedges with the cucumber, shallot, coriander and pomegranate, and pile onto plates. Spoon over a little sauce. Slice the chicken, pile on top of the salad and spoon over the remaining sauce. Eat while the chicken is still warm.</li>
        </ol>
      </div>

      <p class="tip"><strong>TIP:</strong> Leftover chicken keeps well in the fridge for two days, so cook a double batch and pack it into lunch boxes with extra salad leaves and a wedge of lime.</p>

      <span class="brand">Hollinbrook Vale Corp.</span>
    </section>

  </div>
</body>
</html>
```